Web hosting and design company website

Hello
i need a website for my hosting company.
Brindle Peak Servers
http://brindlepeak.example
Should be technical, crisp, corporate and friendly.
needs a products page, contact, about us, portfolio
needs to be a wordpress site
Logo will be provided shortly
colours should be green, yello, blue, white, black

Industry/Entity Type

Information Technology

Coding

Coded - Design and coding required

Number of Pages Required

4 page

Font styles to use
Sans Serif

Colors
fbee3d
fbf289
acd036
cadf82
0692cd
33a6d7
0355a3
faa54b

Requirements
Must have
• about us
• contact us
• products
• portfolio

```html
<!DOCTYPE html>
<html lang="en">
<head>
<meta charset="utf-8">
<title>Brindle Peak Servers</title>
<link rel="stylesheet" href="https://fonts.googleapis.com/css2?family=Lato:wght@300;400;700;900&family=Open+Sans:wght@400;600;700&display=swap">
<style>
:root{
  --blue:#2536ae;
  --blue-dark:#1d2c93;
  --yellow:#f7cb0c;
  --yellow-deep:#efc300;
  --ink:#333;
  --muted:#6a6a6a;
  --line:#dcdcdc;
  --dark:#1c1c1c;
  --white:#fff;
}
*{margin:0;padding:0;box-sizing:border-box}
html,body{width:699px;height:1200px;overflow:hidden;background:var(--white)}
body{font-family:"Open Sans",Arial,sans-serif;color:var(--ink);position:relative}
.abs{position:absolute}
.page{position:relative;width:699px;height:1200px;overflow:hidden}

/* header */
.topbar{left:0;top:0;width:699px;height:20px;background:linear-gradient(#2b2b2b,#0d0d0d)}
.logo-tab{left:116px;top:0;width:38px;height:20px;background:var(--white);border-radius:0 0 19px 19px}
.logo-dot{left:126px;top:3px;width:18px;height:14px;border-radius:50%;background:var(--yellow)}
.brand-head{left:96px;top:24px;font:700 8.5px "Lato",sans-serif;color:var(--blue);letter-spacing:.2px}
.nav{right:99px;top:0;height:20px;display:flex;gap:0;list-style:none}
.nav li{font:400 5.6px "Open Sans",sans-serif;color:var(--white);line-height:20px;padding:0 9px;text-transform:uppercase;border-left:1px solid rgba(255,255,255,.08)}
.nav li:first-child{border-left:0}

/* hero */
.hero{left:0;top:20px;width:699px;height:205px;background:linear-gradient(90deg,#f1f1f1,#fafafa 45%,#ececec)}
.hero-server{left:82px;top:56px;width:176px;height:140px;border-radius:12px;background:radial-gradient(circle at 55% 45%,#4a4a4a,#151515 70%)}
.hero-kicker{left:380px;top:64px;font:900 19px/24px "Lato",sans-serif;color:var(--yellow);letter-spacing:.5px}
.hero-title{left:379px;top:118px;font:700 30px "Lato",sans-serif;color:var(--blue);letter-spacing:.3px}
.hero-sub{left:380px;top:152px;font:300 15.5px "Lato",sans-serif;color:#555;letter-spacing:.4px}
.btn-shop{left:380px;top:182px;width:84px;height:19px;border-radius:10px;background:var(--blue);color:var(--white);font:400 9px/19px "Open Sans",sans-serif;padding-left:12px}
.btn-shop svg{position:absolute;right:4px;top:3px}

/* domains */
.section-title{width:699px;text-align:center;font:300 13px "Lato",sans-serif;color:#444;letter-spacing:.5px}
.domain-sub{top:276px;width:699px;text-align:center;font:400 8px "Open Sans",sans-serif;color:var(--blue)}
.domain-table{left:95px;top:298px;width:510px;height:70px;border:1px solid var(--line);border-radius:3px;display:flex;overflow:hidden}
.tld{width:85px;border-right:1px solid var(--line);text-align:center}
.tld-name{height:34px;line-height:34px;font:600 10.5px "Open Sans",sans-serif;color:#444;border-bottom:1px solid var(--line)}
.tld-old{font:400 6px "Open Sans",sans-serif;color:#aaa;text-decoration:line-through;margin-top:6px}
.tld-new{font:700 8px "Open Sans",sans-serif;color:var(--blue);margin-top:2px}
.buy{flex:1;background:var(--yellow);color:var(--white);text-align:center;font:900 11.5px/15px "Lato",sans-serif;padding-top:20px}

/* services */
.services{left:0;top:402px;width:699px;height:171px;background:linear-gradient(135deg,#2838b4,#2332a6 50%,#2a3bb8)}
.services .section-title{top:21px;color:var(--white)}
.notch{left:326px;top:402px}
.service{width:150px;height:44px}
.service-icon{position:absolute;left:0;top:0;width:42px;height:42px;border-radius:50%;border:2px solid rgba(255,255,255,.85)}
.service h3{position:absolute;left:55px;top:3px;font:700 8.5px "Open Sans",sans-serif;color:var(--white)}
.service p{position:absolute;left:55px;top:15px;width:95px;font:400 4.6px/6.5px "Open Sans",sans-serif;color:#dfe3ff}

/* plans */
.plans .section-title{top:592px}
.plan-table{left:95px;top:622px;width:510px;height:184px;border:1px solid var(--line);border-radius:3px;background:var(--white)}
.plan-col{top:0;height:183px;border-right:1px solid var(--line)}
.plan-col:last-child{border-right:0}
.plan-name{position:absolute;top:0;width:100%;height:36px;line-height:36px;text-align:center;font:400 8px "Open Sans",sans-serif;color:#444}
.ribbon{left:75px;top:658px}
.price{top:658px;height:42px;text-align:center;color:#111}
.price b{font:900 23px "Lato",sans-serif;letter-spacing:-.5px}
.price sup,.price .cents{font:900 11px "Lato",sans-serif}
.price sup{vertical-align:7px}
.price small{display:block;font:900 6.5px "Lato",sans-serif;margin-top:-4px}
.feature{left:95px;width:510px;height:22px}
.feature.alt{background:#ececec}
.feature.light{background:#f6f6f6}
.feat-text{width:100%;height:100%;display:flex}
.feat-text span{flex:none;text-align:center;font:400 5.8px/22px "Open Sans",sans-serif;color:#444}
.order{top:778px;width:62px;height:18px;border-radius:9px;background:var(--blue);color:var(--white);font:400 7.5px/18px "Open Sans",sans-serif;text-align:center}

/* testimonials */
.testimonials{left:0;top:838px;width:699px;height:190px;background:linear-gradient(135deg,#262626,#151515 60%,#222)}
.testimonials .section-title{top:28px;color:var(--white)}
.client-photo{left:306px;top:45px;width:82px;height:82px;border-radius:50%;border:2px solid var(--white);background:radial-gradient(circle at 40% 40%,#c9cbd0,#8a9099)}
.arrow-btn{top:101px;width:34px;height:34px;border-radius:50%;background:#333}
.arrow-btn svg{position:absolute;left:11px;top:9px}
.quote{left:110px;top:142px;width:479px;text-align:center;font:400 7px/10px "Open Sans",sans-serif;color:var(--white)}
.quote-name{top:167px;width:699px;text-align:center;font:400 6.3px "Open Sans",sans-serif;color:var(--yellow);text-transform:uppercase}

/* newsletter */
.newsletter{left:0;top:1028px;width:699px;height:74px;background:var(--yellow-deep)}
.news-icon{left:96px;top:18px}
.news-kicker{left:95px;top:32px;font:400 7.5px "Lato",sans-serif;color:#222}
.news-title{left:95px;top:42px;font:400 13.5px "Lato",sans-serif;color:#222;letter-spacing:.8px}
.news-input{left:190px;top:34px;width:337px;height:20px;background:var(--white);border-radius:2px}
.news-btn{left:531px;top:34px;width:74px;height:20px;background:var(--blue);color:var(--white);font:400 8px/20px "Open Sans",sans-serif;text-align:center;border-radius:2px}

/* footer */
.footer{left:0;top:1102px;width:699px;height:98px;background:var(--white)}
.foot-dot{left:96px;top:24px;width:14px;height:14px;border-radius:50%;background:var(--yellow)}
.foot-brand{left:116px;top:25px;font:400 8.5px "Lato",sans-serif;color:var(--blue)}
.copyright{left:97px;top:42px;font:400 5.5px "Open Sans",sans-serif;color:#444}
.foot-head{top:13px;font:700 7px "Open Sans",sans-serif;color:#222}
.foot-links{list-style:none;font:400 5.5px/10.5px "Open Sans",sans-serif;color:#555}
.foot-text{font:400 5.3px/7.5px "Open Sans",sans-serif;color:#555}
.social{left:530px;width:14px;height:14px;background:#3a3a3a;border-radius:2px}
</style>
</head>
<body>
<div class="page">

  <!-- header -->
  <header>
    <div class="abs topbar"></div>
    <div class="abs logo-tab"></div>
    <div class="abs logo-dot"></div>
    <div class="abs brand-head">BRINDLE PEAK SERVERS</div>
    <ul class="abs nav">
      <li>Home</li><li>About</li><li>FAQs</li><li>Hosting</li><li>Our Services</li><li>Contact Us</li>
    </ul>
  </header>

  <!-- hero -->
  <section>
    <div class="abs hero" role="img" aria-label="Bright data centre corridor with server racks"></div>
    <div class="abs hero-server" role="img" aria-label="Black rack-mount server units"></div>
    <div class="abs hero-kicker">PROFESSIONAL<br>EMAIL</div>
    <h1 class="abs hero-title">SOLUTIONS</h1>
    <div class="abs hero-sub">FOR YOUR HOME OR BUSINESS</div>
    <div class="abs btn-shop">SHOP NOW!
      <svg width="13" height="13" viewBox="0 0 13 13"><circle cx="6.5" cy="6.5" r="6.5" fill="#f7cb0c"/><path d="M5 3.5 8 6.5 5 9.5" fill="none" stroke="#2536ae" stroke-width="1.6"/></svg>
    </div>
  </section>

  <!-- domains -->
  <section>
    <h2 class="abs section-title" style="top:256px">GET A DOMAIN NAME</h2>
    <div class="abs domain-sub">Get Domain Names with FREE Email Accounts</div>
    <div class="abs domain-table">
      <div class="tld"><div class="tld-name">.net</div><div class="tld-old">399</div><div class="tld-new">299</div></div>
      <div class="tld"><div class="tld-name">.com</div><div class="tld-old">723</div><div class="tld-new">623</div></div>
      <div class="tld"><div class="tld-name">.org</div><div class="tld-old">349</div><div class="tld-new">249</div></div>
      <div class="tld"><div class="tld-name">.biz</div><div class="tld-old">239</div><div class="tld-new">139</div></div>
      <div class="tld"><div class="tld-name">.me</div><div class="tld-old">299</div><div class="tld-new">199</div></div>
      <div class="buy">BUY<br>NOW!</div>
    </div>
  </section>

  <!-- services -->
  <section class="abs services">
    <h2 class="abs section-title">OUR SERVICES</h2>
    <div class="abs service" style="left:96px;top:54px"><div class="service-icon" style="background:#e84a4a" role="img" aria-label="Hosting server icon"></div><h3>Fast Web Hosting</h3><p>Lorem ipsum dolor sit amet conse ctetur adipisicing elit, sed do eiusmod tempor incididunt ut labore.</p></div>
    <div class="abs service" style="left:280px;top:54px"><div class="service-icon" style="background:#24324f" role="img" aria-label="Presentation board icon"></div><h3>Data Analysis</h3><p>Lorem ipsum dolor sit amet conse ctetur adipisicing elit, sed do eiusmod tempor incididunt ut labore.</p></div>
    <div class="abs service" style="left:459px;top:54px"><div class="service-icon" style="background:linear-gradient(90deg,#2bb08f 50%,#f1c40f 50%)" role="img" aria-label="Hardware equipment icon"></div><h3>Quality Equipment</h3><p>Lorem ipsum dolor sit amet conse ctetur adipisicing elit, sed do eiusmod tempor incididunt ut labore.</p></div>
    <div class="abs service" style="left:96px;top:112px"><div class="service-icon" style="background:#f4c41b" role="img" aria-label="Wrench icon"></div><h3>Technical Service</h3><p>Lorem ipsum dolor sit amet conse ctetur adipisicing elit, sed do eiusmod tempor incididunt ut labore.</p></div>
    <div class="abs service" style="left:280px;top:112px"><div class="service-icon" style="background:#17b3e6" role="img" aria-label="Alarm bell icon"></div><h3>Daily Backups</h3><p>Lorem ipsum dolor sit amet conse ctetur adipisicing elit, sed do eiusmod tempor incididunt ut labore.</p></div>
    <div class="abs service" style="left:459px;top:112px"><div class="service-icon" style="background:#e9e9e9" role="img" aria-label="Shirt and tie icon"></div><h3>24/7 Support</h3><p>Lorem ipsum dolor sit amet conse ctetur adipisicing elit, sed do eiusmod tempor incididunt ut labore.</p></div>
  </section>
  <svg class="abs notch" width="46" height="12" viewBox="0 0 46 12"><path d="M0 0H46C38 0 34 2 30 7 27 11 19 11 16 7 12 2 8 0 0 0Z" fill="#fff"/></svg>

  <!-- plans -->
  <section class="plans">
    <h2 class="abs section-title">HIGH-SPEED HOSTING SOLUTIONS</h2>
    <div class="abs plan-table">
      <div class="abs plan-col" style="left:0;width:123px"><div class="plan-name">BRONZE</div></div>
      <div class="abs plan-col" style="left:123px;width:131px"><div class="plan-name">SLIVER</div></div>
      <div class="abs plan-col" style="left:254px;width:131px"><div class="plan-name">GOLD</div></div>
      <div class="abs plan-col" style="left:385px;width:124px"><div class="plan-name">PLATINUM</div></div>
    </div>
    <svg class="abs ribbon" width="551" height="42" viewBox="0 0 551 42"><path d="M0 0H551L540 21 551 42H0L11 21Z" fill="#f7cb0c"/></svg>
    <div class="abs price" style="left:95px;width:123px"><sup>$</sup><b>10</b><span class="cents">.89</span><small>MONTH</small></div>
    <div class="abs price" style="left:218px;width:131px"><sup>$</sup><b>20</b><span class="cents">.89</span><small>MONTH</small></div>
    <div class="abs price" style="left:349px;width:131px"><sup>$</sup><b>40</b><span class="cents">.89</span><small>MONTH</small></div>
    <div class="abs price" style="left:480px;width:125px"><sup>$</sup><b>60</b><span class="cents">.89</span><small>MONTH</small></div>
    <div class="abs feature alt" style="top:700px"><div class="feat-text"><span style="width:123px">256 MB Memory</span><span style="width:131px">256 MB Memory</span><span style="width:131px">256 MB Memory</span><span style="width:125px">256 MB Memory</span></div></div>
    <div class="abs feature light" style="top:722px"><div class="feat-text"><span style="width:123px">10 SSG Space</span><span style="width:131px">10 SSG Space</span><span style="width:131px">10 SSG Space</span><span style="width:125px">10 SSG Space</span></div></div>
    <div class="abs feature alt" style="top:745px"><div class="feat-text"><span style="width:123px">Unmetered Bendwidth</span><span style="width:131px">Unmetered Bendwidth</span><span style="width:131px">Unmetered Bendwidth</span><span style="width:125px">Unmetered Bendwidth</span></div></div>
    <div class="abs order" style="left:124px">Order Now</div>
    <div class="abs order" style="left:253px">Order Now</div>
    <div class="abs order" style="left:383px">Order Now</div>
    <div class="abs order" style="left:512px">Order Now</div>
  </section>

  <!-- testimonials -->
  <section class="abs testimonials">
    <h2 class="abs section-title">WHAT PEOPLE SAY ABOUT US</h2>
    <div class="abs client-photo" role="img" aria-label="Portrait of a smiling client in an office"></div>
    <div class="abs arrow-btn" style="left:77px"><svg width="10" height="16" viewBox="0 0 10 16"><path d="M8 1 2 8 8 15" fill="none" stroke="#666" stroke-width="1.2"/></svg></div>
    <div class="abs arrow-btn" style="left:585px"><svg width="10" height="16" viewBox="0 0 10 16"><path d="M2 1 8 8 2 15" fill="none" stroke="#666" stroke-width="1.2"/></svg></div>
    <p class="abs quote">“Lorem ipsum dolor sit amet, conse dolorop eturetu adipiscing elit. Duisvel nisifes ipsu. Vestibul ullamcorp dolore. Lorem ipsum dolor sit amet, conse dolorop eturetu adipiscing elit. Duisvel nisifes ipsu. Vestibul ullamcorp dolore.”</p>
    <div class="abs quote-name">Vestibul Ullamcorp Dolore.</div>
  </section>

  <!-- newsletter -->
  <section class="abs newsletter">
    <svg class="abs news-icon" width="10" height="7" viewBox="0 0 10 7"><rect x=".5" y=".5" width="9" height="6" fill="none" stroke="#333" stroke-width=".8"/><path d="M.5.5 5 4 9.5.5" fill="none" stroke="#333" stroke-width=".8"/></svg>
    <div class="abs news-kicker">SIGN UP YOUR</div>
    <div class="abs news-title">NEWSLETTER</div>
    <div class="abs news-input"></div>
    <div class="abs news-btn">SIGN UP NOW</div>
  </section>

  <!-- footer -->
  <footer class="abs footer">
    <div class="abs foot-dot"></div>
    <div class="abs foot-brand">BRINDLE PEAK SERVERS</div>
    <div class="abs copyright">© 2015 Brindle Peak Servers. All Rights Reserved.</div>

    <div class="abs foot-head" style="left:236px">Quick Links</div>
    <ul class="abs foot-links" style="left:238px;top:26px"><li>Home</li><li>About</li><li>Faqs</li></ul>
    <ul class="abs foot-links" style="left:312px;top:26px"><li>Hosting</li><li>Our Services</li><li>Contact Us</li></ul>

    <div class="abs foot-head" style="left:381px">Contact</div>
    <p class="abs foot-text" style="left:381px;top:25px;width:125px">Ridgeline is a simple yet highly configurable theme for a web store.</p>
    <svg class="abs" style="left:381px;top:43px" width="6" height="6" viewBox="0 0 6 6"><path d="M0 3 3 0 6 3H5V6H1V3Z" fill="#444"/></svg>
    <p class="abs foot-text" style="left:393px;top:41px;width:120px">PEAKLINE LTD., 42 QUARRY LANE,<br>DUNMORE, DK7 2QP</p>
    <svg class="abs" style="left:381px;top:74px" width="5" height="7" viewBox="0 0 5 7"><rect x=".5" y=".5" width="4" height="6" rx=".6" fill="none" stroke="#444" stroke-width=".7"/></svg>
    <p class="abs foot-text" style="left:393px;top:73px">+ 555-0142-3310, + 555-0142-3311</p>

    <div class="abs foot-head" style="left:530px">Social Media</div>
    <div class="abs social" style="top:32px"></div>
    <div class="abs social" style="top:51px"></div>
    <div class="abs social" style="top:70px"></div>
  </footer>

</div>
</body>
</html>
```